Business card design reauest

2 sided. White on both sides

Gordon Mabry

Ho Chi Minh, Vietnam

Cell Phone / Whatsapp/ Wechat/Zalo
1-555-382-7194
Gmabry@kwpartsworks.vn
Www.kwpartsworks.vn
Www.kwpartsworks.com

Industry/Entity Type

Sofa and furniture and kitchen

Contact Information for Business Card

2 sided. White on both sides Gordon Mabry Ho Chi Minh, Vietnam Cell Phone / Whatsapp/ Wechat/Zalo 1-555-382-7194 Gmabry@kwpartsworks.vn Www.kwpartsworks.vn Www.kwpartsworks.com

```html
<!DOCTYPE html>
<html lang="en">
<head>
<meta charset="utf-8">
<title>Kingswood Parts Works – Business Card</title>
<link href="https://fonts.googleapis.com/css2?family=Lato:wght@400;700;900&display=swap" rel="stylesheet">
<style>
  :root {
    --bg: #4a4a4a;
    --card: #ffffff;
    --green: #0f9a3a;
    --ink: #1f1f1f;
    --rule: #2a2a2a;
  }
  * { margin: 0; padding: 0; box-sizing: border-box; }
  html, body { width: 1200px; height: 694px; overflow: hidden; }
  body {
    background: var(--bg);
    font-family: 'Lato', Arial, sans-serif;
    position: relative;
  }
  .card {
    position: absolute;
    top: 193px;
    width: 540px;
    height: 308px;
    background: var(--card);
    box-shadow: 0 10px 28px rgba(0,0,0,.35);
    overflow: hidden;
  }
  .card--front { left: 40px; }
  .card--back { left: 620px; }

  /* Front */
  .front-brand {
    position: absolute;
    inset: 0;
    display: flex;
    flex-direction: column;
    align-items: center;
    justify-content: center;
    gap: 14px;
  }
  .brand-mark {
    width: 58px; height: 58px;
    border: 6px solid var(--green);
    border-radius: 50%;
  }
  .brand-name {
    color: var(--green);
    font-weight: 700;
    font-size: 40px;
    letter-spacing: 3px;
    text-transform: uppercase;
    text-align: center;
    line-height: 1.1;
  }

  /* Back */
  .back-brand {
    position: absolute;
    top: 30px;
    right: 34px;
    display: flex;
    align-items: center;
    gap: 8px;
  }
  .back-brand .brand-mark { width: 24px; height: 24px; border-width: 3px; }
  .back-brand .brand-name { font-size: 19px; letter-spacing: 1.5px; }
  .divider {
    position: absolute;
    left: 30px; right: 30px; top: 102px;
    height: 1px; background: var(--rule);
  }
  .person {
    position: absolute;
    left: 30px; top: 116px;
  }
  .person-name {
    color: var(--green);
    font-weight: 900;
    font-size: 24px;
  }
  .person-role {
    color: var(--ink);
    font-size: 15px;
    margin-top: 2px;
  }
  .contacts {
    position: absolute;
    left: 30px; top: 172px;
    list-style: none;
  }
  .contact {
    display: flex;
    align-items: center;
    gap: 8px;
    color: var(--ink);
    font-size: 13px;
    line-height: 19px;
  }
  .contact svg { width: 13px; height: 13px; fill: var(--green); flex: none; }
  .band { position: absolute; left: 0; bottom: 0; width: 540px; height: 308px; }
  .location {
    position: absolute;
    right: 22px; bottom: 24px;
    color: #fff;
    font-size: 15px;
  }
</style>
</head>
<body>

<section class="card card--front" aria-label="Card front">
  <div class="front-brand">
    <span class="brand-mark"></span>
    <span class="brand-name">Kingswood<br>Parts Works</span>
  </div>
</section>

<section class="card card--back" aria-label="Card back">
  <svg class="band" viewBox="0 0 540 308" aria-hidden="true">
    <polygon points="318,246 540,246 540,308 0,308 0,300 302,300" fill="var(--green)"/>
    <polygon points="0,284 296,284 306,270 313,270 300,294 0,294" fill="var(--ink)"/>
  </svg>

  <div class="back-brand">
    <span class="brand-mark"></span>
    <span class="brand-name">Kingswood Parts Works</span>
  </div>
  <div class="divider"></div>

  <div class="person">
    <div class="person-name">Gordon Mabry</div>
    <div class="person-role">Owner</div>
  </div>

  <ul class="contacts">
    <li class="contact">
      <svg viewBox="0 0 24 24"><path d="M6.6 10.8a15 15 0 0 0 6.6 6.6l2.2-2.2a1 1 0 0 1 1-.25 11.4 11.4 0 0 0 3.6.57 1 1 0 0 1 1 1V20a1 1 0 0 1-1 1A17 17 0 0 1 3 4a1 1 0 0 1 1-1h3.5a1 1 0 0 1 1 1c0 1.25.2 2.45.57 3.57a1 1 0 0 1-.25 1z"/></svg>
      Cell Phone / Whatsapp/ Wechat/Zalo 1-555-382-7194
    </li>
    <li class="contact">
      <svg viewBox="0 0 24 24"><path d="M2 5h20v14H2z M2 5l10 8 10-8" fill="var(--green)" stroke="#fff" stroke-width="1.5"/></svg>
      Gmabry@kwpartsworks.vn
    </li>
    <li class="contact">
      <svg viewBox="0 0 24 24"><circle cx="12" cy="12" r="10"/><path d="M2 12h20M12 2c3 3 3 17 0 20M12 2c-3 3-3 17 0 20" stroke="#fff" stroke-width="1.4" fill="none"/></svg>
      Www.kwpartsworks.vn
    </li>
    <li class="contact">
      <svg viewBox="0 0 24 24"><circle cx="12" cy="12" r="10"/><path d="M2 12h20M12 2c3 3 3 17 0 20M12 2c-3 3-3 17 0 20" stroke="#fff" stroke-width="1.4" fill="none"/></svg>
      Www.kwpartsworks.com
    </li>
  </ul>

  <div class="location">Ho Chi Minh, Vietnam</div>
</section>

</body>
</html>
```